Bellwether Recovery Brochure for a drug and alcohol addiction treatment center.

***Update #2***
For graphic highlights no intrusion into text and no fade into adjoining areas.Use modern clean white layout with grey and light orange color scheme. Use attached yoga photo and other photos. For cover try moving number and logo around, and also try with cover photo not full size. Also use larger text with bullet points in a couple spots. Also try with new attached cover photos.
***Update*** I have attached some new photos to clarify the design wanted. My client likes the size (but not design) of the brochure in the newly included photos. Note the measurements - when closed it is 6" wide x 7" tall. When fully open it is 18" long, 7" wide, with 2 folds. I apologize if my terminology below was confusing. Please confirm that your design reflects the desired layout, and please modify your design if it does not. Thanks!
Want a trifold brochure 6" wide x 7" height. Design is for a drug and alcohol addiction treatment center. We want clean, soft, contemporary with highlight colors orange and grey, with contemporary font. Maybe some soft curves on design - see this A4 design we like but not the colors:
http://quillstockmart.net/item/business-trifold-brochure-wave/7315920?s_phrase=trifold%20business%20brochure&s_rank=54
See company web site for style cues and some content you can use:
http://bellwetherrecovery.com/
You can use the attached photos and logo in the design. Try sun in hand photo on cover, or man on beach. Please do not use the words "The Bellwether Recovery Center" in verbiage or titles, for business reasons we want to use "Bellwether Recovery Center" with no "The" instead.
Please note that the logo has been updated. The new logo is attached below. Use bellwether rev2.png for logo.
Addiction treatment industry professionals; family and decision makers of addict; addict themselves.

```html
<!DOCTYPE html>
<html lang="en">
<head>
<meta charset="utf-8">
<title>Bellwether Recovery Center – Trifold Brochure</title>
<link rel="stylesheet" href="https://fonts.googleapis.com/css2?family=Questrial&family=Open+Sans:ital,wght@0,400;0,700;1,400;1,700&display=swap">
<style>
  :root {
    --orange: #f08a24;
    --orange-deep: #e8641f;
    --orange-light: #f6a445;
    --grey: #555555;
    --grey-light: #8a8a8a;
    --white: #ffffff;
    --page: #e9e9e9;
    --heading: "Questrial", "Century Gothic", sans-serif;
    --body: "Open Sans", Arial, sans-serif;
  }
  * { box-sizing: border-box; margin: 0; padding: 0; }
  html, body { width: 1200px; height: 1025px; overflow: hidden; background: var(--page); }
  body { position: relative; font-family: var(--body); color: var(--grey); }

  .spread {
    position: absolute; left: 60px; width: 1080px; height: 420px;
    display: flex; box-shadow: 0 6px 18px rgba(0,0,0,.18); overflow: hidden;
  }
  .spread--outside { top: 50px; }
  .spread--inside { top: 545px; }

  .panel { position: relative; width: 360px; height: 420px; overflow: hidden; }
  .panel--white { background: var(--white); }
  .panel--orange { background: linear-gradient(160deg, var(--orange-light), var(--orange) 55%, var(--orange-deep)); color: var(--white); }

  .photo {
    position: absolute; border-radius: 50%; border: 4px solid var(--white);
    box-shadow: 6px 6px 0 var(--orange-deep);
  }
  .photo--room { background: radial-gradient(circle at 40% 40%, #d9cdb8, #8f8372); }
  .photo--group { background: radial-gradient(circle at 55% 40%, #cfc7bf, #6d6158); }
  .photo--beach { background: linear-gradient(180deg, #f7d27a 0%, #f3a43a 45%, #c7781f 60%, #f4c15a 100%); }
  .photo--couple { background: radial-gradient(circle at 50% 45%, #e3d6cc, #8a7766); }
  .photo--worried { background: radial-gradient(circle at 45% 45%, #d8d8d8, #9a9a9a); }
  .photo--yoga { background: linear-gradient(180deg, #fbe1a3 0%, #f2a84a 50%, #7d8fa0 80%, #c9a88a 100%); }

  h2, h3 { font-family: var(--heading); font-weight: 400; line-height: 1.05; }
  p { font-size: 8.5px; line-height: 1.42; }
  .text-block { position: absolute; }
  .text-block p + p { margin-top: 7px; }
  .gap { margin-top: 7px; }

  /* outside */
  .about-title { font-size: 28px; color: var(--orange); }
  .about-title span { color: var(--grey); }
  .about-copy p { font-style: italic; }
  .about-copy strong { font-weight: 700; }

  .care-title { font-size: 30px; color: var(--white); line-height: 1.15; }
  .care-contact p { font-size: 10px; color: var(--white); }
  .care-contact strong { font-size: 12.5px; }
  .side-url {
    position: absolute; right: 8px; bottom: 20px; font-size: 9px; color: var(--white);
    writing-mode: vertical-rl;
  }

  .brand { position: absolute; top: 22px; right: 18px; display: flex; align-items: center; gap: 8px; }
  .brand-dot { width: 26px; height: 26px; border-radius: 50%; background: var(--grey); }
  .brand-name { font-family: var(--heading); font-size: 13px; color: var(--grey); line-height: 1.1; width: 120px; }
  .cover-url { position: absolute; left: 38px; bottom: 58px; font-size: 11px; color: var(--grey); }
  .cover-title { position: absolute; right: 20px; bottom: 60px; text-align: right; font-family: var(--heading); font-weight: 400; }
  .cover-title .accent { display: block; font-size: 28px; color: var(--orange-deep); font-family: var(--body); font-weight: 700; }
  .cover-title .rest { display: block; font-size: 25px; color: var(--grey); }

  /* inside */
  .light-title { font-size: 24px; color: var(--white); }
  .light-sub { font-size: 15px; color: var(--white); }
  .phone { font-weight: 700; font-size: 11.5px; margin-top: 5px; }
  .dark-title { font-size: 21px; color: var(--orange-deep); }
  .dark-sub { font-size: 15px; color: var(--orange-deep); }
  .finance-title { font-size: 32px; color: var(--white); text-align: center; line-height: 1.05; }
  .benefits { list-style: none; }
  .benefits li { display: flex; align-items: center; gap: 7px; font-size: 10px; line-height: 1.2; color: var(--white); margin-bottom: 7px; }
  .benefits svg { width: 11px; height: 11px; flex: none; }
</style>
</head>
<body>

<section class="spread spread--outside" aria-label="Brochure outside">
  <div class="panel panel--white">
    <div class="photo photo--room" role="img" aria-label="Photo of a treatment center group room" style="left:28px;top:26px;width:124px;height:124px;"></div>
    <div class="photo photo--group" role="img" aria-label="Photo of a counselor leading a group session" style="left:170px;top:12px;width:144px;height:144px;"></div>
    <div class="text-block about-copy" style="left:26px;top:172px;width:316px;">
      <h2 class="about-title">About <span>Us</span></h2>
      <p class="gap">Bellwether Recovery Center offers affordable treatment for a wide variety of addictions. We address underlying psychological disorders and specialize in treatment for <strong>drug addiction and alcoholism</strong>. At Bellwether Recovery Center we feature a full spectrum of addiction treatment programs, from initial assessment and detox, to inpatient residential and intensive outpatient care, as well as transitional housing and sober living environments for extended care.</p>
      <p>Our clinical team are committed to treating each client with respect and are receptive to each clients' individual needs. Our treatment programs are abstinence based. We provide a comprehensive slate of services, such as individual, group counseling, drug and alcohol educational groups, and an introduction to <strong>12-step programs</strong>. We also offer a strong family support program, recognizing the special importance of family healing in the recovery process.</p>
    </div>
  </div>

  <div class="panel panel--orange">
    <div class="text-block" style="left:28px;top:130px;width:300px;">
      <h2 class="care-title">Quality<br>Addiction<br>Care</h2>
    </div>
    <div class="text-block care-contact" style="left:28px;top:272px;width:280px;">
      <p>Contact Bellwether Recovery Center Today at <strong>855-555-0142</strong>, if you require Auxiliary Aid in communicating with our team please reach out to our call center.</p>
    </div>
    <span class="side-url">bellwetherrecovery.com</span>
  </div>

  <div class="panel panel--white">
    <div class="brand">
      <span class="brand-dot"></span>
      <span class="brand-name">Bellwether Recovery Center</span>
    </div>
    <div class="photo photo--beach" role="img" aria-label="Photo of a man standing on a beach at sunset" style="left:-20px;top:70px;width:230px;height:230px;"></div>
    <span class="cover-url">bellwetherrecovery.com</span>
    <h1 class="cover-title"><span class="accent">Recover</span><span class="rest">from Addiction</span></h1>
  </div>
</section>

<section class="spread spread--inside" aria-label="Brochure inside">
  <div class="panel panel--orange">
    <div class="photo photo--couple" role="img" aria-label="Photo of a smiling couple holding hands" style="left:18px;top:20px;width:132px;height:132px;"></div>
    <div class="text-block" style="left:176px;top:26px;width:168px;">
      <h2 class="light-title">Alcohol<br>Rehab</h2>
      <p class="gap">Our dedicated staff are here to assist you or your loved one with recovery from the struggle of alcoholism. We offer a comprehensive array of programs starting with our residential detox program whenever necessary. Bellwether Recovery Center also offers residential, partial hospitalization and intensive outpatient programs. Family support and trauma recovery are an integral component of our program as well, because we're focused on lifelong success for our clients.</p>
      <p>The alcohol rehab programs focus on building life skills that are necessary for successful, long-term healing. Weekly sessions consist of processing groups as well as substance abuse educational classes. We employ a skilled and experienced staff with a comprehensive and contemporary approach to recovery.</p>
    </div>
    <div class="text-block" style="left:18px;top:180px;width:150px;">
      <h3 class="light-sub">Our Alcohol Rehab Features a Full Spectrum of Services</h3>
      <p class="gap">Bellwether Recovery Center in sunny and beautiful Southern California is always available for you or your loved one to help start the journey of recovery from drug addiction or alcoholism. If you or someone you love is struggling with alcoholism or addiction, call us today at</p>
      <p class="phone">855-555-0142.</p>
    </div>
  </div>

  <div class="panel panel--white">
    <div class="text-block" style="left:14px;top:24px;width:170px;">
      <h2 class="dark-title">Drug Rehab</h2>
      <p class="gap">At Bellwether Recovery Center, we offer a full array of affordable drug rehab programs that can take addicts from detox to inpatient or outpatient care and back home again. If you or your loved one requires detox from drugs, we take them through our residential detox program, and then after a thorough assessment help him or her determine the best treatment option. This may be residential treatment, partial hospitalization program or intensive outpatient care.</p>
      <p>If detox is not required we may admit someone directly into our residential inpatient program, or possibly suggest intensive outpatient services. One goal is to help each client to develop the life skills he or she needs to be successful after treatment. Our concerned and experienced staff are here to assist in each person through a comprehensive assessment and the entire recovery process, no matter the path chosen.</p>
    </div>
    <div class="photo photo--worried" role="img" aria-label="Photo of a young woman talking with a counselor" style="left:192px;top:12px;width:146px;height:146px;"></div>
    <div class="text-block" style="left:192px;top:178px;width:156px;">
      <h3 class="dark-sub">Drug Addiction Rehab Beginning to End</h3>
      <p class="gap">At Bellwether Recovery Center we also offer a partial hospitalization and an intensive outpatient program. These programs consist primarily of the same activities and therapeutic elements of our residential program, and are also based on the progress of individual clients within the individualized treatment plan that every client prepares with their counselor.</p>
    </div>
  </div>

  <div class="panel panel--orange">
    <div class="text-block" style="left:20px;top:16px;width:320px;">
      <h2 class="finance-title">Financing<br>is Available</h2>
      <p style="margin-top:10px;">It is not uncommon for our clients to lack sufficient health insurance coverage for substance abuse treatment. We are here to help. Bellwether Recovery Center offers financing for detox services and residential drug and alcohol treatment services. Applicants do not need perfect credit and may get instant pre-approval.</p>
    </div>
    <div class="photo photo--yoga" role="img" aria-label="Photo of a woman meditating in a yoga pose by the sea at sunrise" style="left:-18px;top:215px;width:160px;height:160px;"></div>
    <ul class="text-block benefits" style="left:172px;top:176px;width:180px;">
      <li><svg viewBox="0 0 12 12" aria-hidden="true"><circle cx="6" cy="6" r="5.2" fill="none" stroke="#fff" stroke-width="1.2"/><path d="M3.5 6.2l1.7 1.7 3.3-3.6" fill="none" stroke="#fff" stroke-width="1.3"/></svg>Immediate Credit Decisions</li>
      <li><svg viewBox="0 0 12 12" aria-hidden="true"><circle cx="6" cy="6" r="5.2" fill="none" stroke="#fff" stroke-width="1.2"/><path d="M3.5 6.2l1.7 1.7 3.3-3.6" fill="none" stroke="#fff" stroke-width="1.3"/></svg>Competitive Interest Rates</li>
      <li><svg viewBox="0 0 12 12" aria-hidden="true"><circle cx="6" cy="6" r="5.2" fill="none" stroke="#fff" stroke-width="1.2"/><path d="M3.5 6.2l1.7 1.7 3.3-3.6" fill="none" stroke="#fff" stroke-width="1.3"/></svg>Affordable Monthly Payments</li>
      <li><svg viewBox="0 0 12 12" aria-hidden="true"><circle cx="6" cy="6" r="5.2" fill="none" stroke="#fff" stroke-width="1.2"/><path d="M3.5 6.2l1.7 1.7 3.3-3.6" fill="none" stroke="#fff" stroke-width="1.3"/></svg>No Collateral Required</li>
      <li><svg viewBox="0 0 12 12" aria-hidden="true"><circle cx="6" cy="6" r="5.2" fill="none" stroke="#fff" stroke-width="1.2"/><path d="M3.5 6.2l1.7 1.7 3.3-3.6" fill="none" stroke="#fff" stroke-width="1.3"/></svg>No Pre Payment Penalties</li>
      <li><svg viewBox="0 0 12 12" aria-hidden="true"><circle cx="6" cy="6" r="5.2" fill="none" stroke="#fff" stroke-width="1.2"/><path d="M3.5 6.2l1.7 1.7 3.3-3.6" fill="none" stroke="#fff" stroke-width="1.3"/></svg>Easy Loan Application</li>
      <li><svg viewBox="0 0 12 12" aria-hidden="true"><circle cx="6" cy="6" r="5.2" fill="none" stroke="#fff" stroke-width="1.2"/><path d="M3.5 6.2l1.7 1.7 3.3-3.6" fill="none" stroke="#fff" stroke-width="1.3"/></svg>100% Confidential</li>
    </ul>
    <div class="text-block" style="left:172px;top:340px;width:175px;">
      <p>No Collateral Required. Financing available through Bellwether Recovery Center is an unsecured installment loan and does not require collateral.</p>
    </div>
  </div>
</section>

</body>
</html>
```